BOLD ORCHID Personal Training Website.

I am looking for a website design for Word Press URL I already have. I have it as 10 very simple pages. Once home page design is set we can use that look on all other pages. I have uploaded a word document that has an outline of what I am looking for. Please take the time to review this. I want to add this is for a WordPress site.

Target Market(s)

Women 25-55

Industry/Entity Type

Health And Wellness

Coding

Coded - Design and coding required

Number of Pages Required

5+ page

```html
<!DOCTYPE html>
<html lang="en">
<head>
<meta charset="utf-8">
<title>BOLD ORCHID – Personal Training</title>
<link rel="stylesheet" href="https://fonts.googleapis.com/css2?family=Bebas+Neue&family=Montserrat:wght@400;500;600&display=swap">
<style>
:root{
  --red:#e8322a;
  --red-deep:#b41c1c;
  --red-soft:#d95043;
  --ink:#333333;
  --muted:#777777;
  --mist:#ececec;
  --blush:#dcbcbc;
  --night:#2f2f2f;
  --white:#ffffff;
  --line:#d8d8d8;
}
*{box-sizing:border-box;margin:0;padding:0}
html,body{width:1200px;height:3734px;overflow:hidden;background:var(--white)}
body{font-family:"Montserrat",Arial,sans-serif;color:var(--ink);position:relative}
.abs{position:absolute}
.heading{font-family:"Bebas Neue",Impact,sans-serif;font-weight:400;color:var(--red);letter-spacing:1px;line-height:1}
.heading .deep{color:var(--red-deep)}

/* hero */
.hero{left:0;top:0;width:1200px;height:660px;overflow:hidden}
.hero-photo{left:0;top:0;width:1200px;height:660px;background:linear-gradient(110deg,#5b5b5b 0%,#3e3e3e 40%,#2a2a2a 70%,#4a4a4a 100%)}
.hero-shade{left:0;top:0;width:1200px;height:660px;background:rgba(20,20,20,.35)}
.nav{left:82px;top:28px;display:flex;gap:24px;font-size:14px;color:var(--white)}
.nav a{color:var(--white);text-decoration:none;padding-bottom:14px}
.nav a.current{border-bottom:2px solid var(--white)}
.brand{left:0;top:110px;width:1200px;text-align:center}
.brand-dot{display:block;width:58px;height:58px;margin:0 auto 10px;border-radius:50%;background:var(--red)}
.brand-name{font-family:"Bebas Neue",Impact,sans-serif;font-size:40px;color:var(--red);letter-spacing:1px}
.tagline{left:0;top:325px;width:1200px;text-align:center;font-size:56px;line-height:58px;color:var(--red)}
.hero-arrow{top:312px}

/* ask band */
.ask{left:0;top:660px;width:1200px;height:154px;background:linear-gradient(90deg,#a51d1d 0%,#d22f26 55%,#e8382b 100%)}
.ask-text{left:100px;top:50px;font-size:18px;line-height:30px;color:var(--white)}
.ask-btn{left:912px;top:50px;width:208px;height:54px;border-radius:27px;background:var(--white);color:var(--red-deep);font-weight:600;font-size:22px;display:flex;align-items:center;justify-content:center;box-shadow:0 3px 6px rgba(0,0,0,.25)}

/* welcome */
.welcome-title{left:0;top:856px;width:1200px;text-align:center;font-size:52px}
.welcome-copy{left:270px;top:926px;width:660px;text-align:center;font-size:12.5px;line-height:24px;color:var(--muted)}

/* certificates */
.photo{border-radius:12px}
.cert-title{left:0;top:1078px;width:1200px;text-align:center;font-size:26px;color:#555;letter-spacing:1px}
.cert{background:var(--white);border:1px solid #cfcfcf;border-radius:6px;box-shadow:0 1px 4px rgba(0,0,0,.12)}
.cert::before{content:"";position:absolute;left:12%;right:12%;top:18%;height:4px;background:#d2d2d2;box-shadow:0 18px 0 #e2e2e2,0 36px 0 #e2e2e2,0 54px 0 #e2e2e2}
.cert::after{content:"";position:absolute;left:10px;bottom:12px;width:48px;height:14px;border-radius:3px;background:#2c4d8a}
.cert.grey{background:#8a8a8a;border-color:#777}
.cert.grey::before{background:#a9a9a9;box-shadow:none}
.cert.grey::after{left:50%;bottom:auto;top:44%;margin-left:-14px;width:28px;height:28px;background:#b5b5b5}

/* videos */
.videos{left:0;top:1586px;width:1200px;height:518px;background:var(--mist);overflow:hidden}
.videos-title{left:712px;top:44px;font-size:50px}

/* blog */
.blog-title{left:0;top:2156px;width:1200px;text-align:center;font-size:52px}
.post{top:2236px;width:501px;height:334px;overflow:hidden}
.post-photo{left:0;top:0;width:501px;height:334px}
.post-bar{left:0;bottom:0;width:501px;height:84px;background:rgba(30,30,30,.82)}
.post-text{left:22px;top:20px;width:390px;font-size:14.5px;line-height:22px;color:var(--white)}
.post-go{right:18px;top:20px;width:46px;height:46px;border-radius:50%;background:var(--white)}

/* testimonials */
.testimonials{left:0;top:2672px;width:1200px;height:436px;background:var(--mist);overflow:hidden}
.testi-title{left:82px;top:56px;font-size:50px}
.testi-quote{left:78px;top:132px}
.testi-copy{left:82px;top:208px;width:500px;font-size:13px;line-height:24px;color:var(--muted)}
.testi-name{left:82px;top:300px;font-size:15px;color:#555}
.testi-dots{left:78px;top:350px;display:flex;gap:8px}
.testi-dots span{width:44px;height:4px;background:#e0b0aa}
.testi-dots span.on{background:var(--red-deep)}
.testi-photo{left:660px;top:0;width:540px;height:436px;border-radius:300px 0 0 300px/218px 0 0 218px;background:linear-gradient(100deg,#e4574a 0%,#d63a2e 50%,#c32b24 100%)}

/* contact */
.contact-title{left:0;top:3158px;width:1200px;text-align:center;font-size:52px}
.field{height:40px;border-bottom:1px solid var(--line);font-size:13px;color:#666;padding-top:4px}
.send{left:508px;top:3446px;width:184px;height:50px;border-radius:25px;background:var(--red);color:var(--white);font-size:21px;font-weight:500;display:flex;align-items:center;justify-content:center;box-shadow:0 3px 6px rgba(0,0,0,.25)}

/* footer */
.footer{left:0;top:3578px;width:1200px;height:156px;background:var(--night)}
.social{top:34px;width:52px;height:52px;border:1.5px solid #bdbdbd;border-radius:50%}
.copyright{left:0;top:112px;width:1200px;text-align:center;font-size:13px;color:#cfcfcf}
</style>
</head>
<body>

<header class="hero abs">
  <div class="hero-photo abs" role="img" aria-label="Women smiling during a group workout class"></div>
  <div class="hero-shade abs"></div>
  <nav class="nav abs">
    <a class="current">Home</a><a>Certifications</a><a>Bio</a><a>Blog</a><a>Videos</a><a>Online Training</a><a>Functional Movement Screening</a><a>Nutrition</a><a>Merchandise</a><a>Contact</a>
  </nav>
  <div class="brand abs"><span class="brand-dot"></span><span class="brand-name">BOLD ORCHID</span></div>
  <h1 class="tagline heading abs">IF IT DOESN'T CHALLANGE YOU,<br>IT WAN'T CHANGE YOU</h1>
  <svg class="hero-arrow abs" style="left:22px" width="40" height="34" viewBox="0 0 40 34" fill="none" stroke="#fff" stroke-width="3" stroke-linejoin="round"><path d="M16 4 3 17l13 13M3 17h22c8 0 12 5 12 12"/></svg>
  <svg class="hero-arrow abs" style="left:1138px" width="40" height="34" viewBox="0 0 40 34" fill="none" stroke="#fff" stroke-width="3" stroke-linejoin="round"><path d="M24 4l13 13-13 13M37 17H15C7 17 3 22 3 29"/></svg>
</header>

<section class="ask abs">
  <p class="ask-text abs">If you have any questions in your mind about training then ask to Maren<br>we will reach you as soon as possible</p>
  <div class="ask-btn abs">ASK NOW</div>
</section>

<section>
  <h2 class="welcome-title heading abs">WELCOME TO <span class="deep">BOLD ORCHID</span></h2>
  <p class="welcome-copy abs">Lorem Ipsum is simply dummy text of the printing and typesetting industry. Lorem Ipsum has been the industry's standard dummy text ever since the 1500s, when an unknown printer took a galley of type and scrambled it to make a type specimen book. It has survived not only five centuries, but also the leap into electronic typesetting, remaining essentially unchanged.</p>

  <div class="photo abs" style="left:0;top:1071px;width:219px;height:294px;background:linear-gradient(135deg,#9a9a9a,#5d5d5d)" role="img" aria-label="Man and woman lifting dumbbells overhead"></div>
  <div class="photo abs" style="left:70px;top:1397px;width:149px;height:105px;background:linear-gradient(135deg,#7a7a7a,#2e2e2e)" role="img" aria-label="Barbell plates close up"></div>
  <div class="photo abs" style="left:986px;top:1068px;width:144px;height:107px;background:linear-gradient(135deg,#4a4a4a,#1e1e1e)" role="img" aria-label="Rack of dumbbells"></div>
  <div class="photo abs" style="left:986px;top:1203px;width:214px;height:296px;background:linear-gradient(135deg,#8c7a7a,#4f5a66)" role="img" aria-label="Women doing squats in a fitness class"></div>
  <div class="photo abs" style="left:740px;top:1404px;width:214px;height:88px;background:linear-gradient(90deg,#8a8a8a,#3a3a3a)" role="img" aria-label="Dumbbells on a gym floor"></div>

  <h3 class="cert-title abs">CERTIFICATES</h3>
  <div class="cert abs" style="left:249px;top:1165px;width:214px;height:155px"></div>
  <div class="cert abs" style="left:493px;top:1165px;width:214px;height:155px"></div>
  <div class="cert abs" style="left:740px;top:1140px;width:214px;height:232px"></div>
  <div class="cert abs" style="left:249px;top:1347px;width:214px;height:155px"></div>
  <div class="cert grey abs" style="left:493px;top:1377px;width:214px;height:117px"></div>
</section>

<section class="videos abs">
  <div class="abs" style="left:-174px;top:-17px;width:548px;height:548px;border-radius:50%;background:linear-gradient(120deg,#e7604e,#c8342a)" role="img" aria-label="Woman lifting a barbell, red tinted"></div>
  <div class="abs" style="left:822px;top:107px;width:548px;height:548px;border-radius:50%;background:var(--blush)"></div>
  <h2 class="videos-title heading abs">VIDEOS</h2>
  <svg class="abs" style="left:420px;top:120px" width="690" height="320" viewBox="0 0 690 320">
    <g role="img" aria-label="Workout video thumbnails">
      <polygon points="108,8 200,100 108,192 16,100" fill="#6b6b6b"/>
      <polygon points="338,8 430,100 338,192 246,100" fill="#8a7f7a"/>
      <polygon points="568,8 660,100 568,192 476,100" fill="#5a4a4a"/>
      <polygon points="223,123 315,215 223,307 131,215" fill="#3d5a78"/>
      <polygon points="453,123 545,215 453,307 361,215" fill="#7f8a94"/>
    </g>
    <path d="M556 84v32l26-16z" fill="none" stroke="#e8322a" stroke-width="4" stroke-linejoin="round"/>
  </svg>
</section>

<section>
  <h2 class="blog-title heading abs">BLOG <span class="deep">POST</span></h2>
  <article class="post abs" style="left:77px">
    <div class="post-photo abs" style="background:linear-gradient(135deg,#9a9a9a,#4d4d4d)" role="img" aria-label="Trainer coaching a client on a rowing machine"></div>
    <div class="post-bar abs">
      <p class="post-text abs">Lorem Ipsum is simply dummy text of the printing and typesetting industry Lorem Ipsum.</p>
      <svg class="post-go abs" viewBox="0 0 46 46"><circle cx="23" cy="23" r="23" fill="#fff"/><path d="M14 23h17M24 15l8 8-8 8" fill="none" stroke="#222" stroke-width="3.5" stroke-linecap="round" stroke-linejoin="round"/></svg>
    </div>
  </article>
  <article class="post abs" style="left:622px">
    <div class="post-photo abs" style="background:linear-gradient(135deg,#a39086,#55504c)" role="img" aria-label="Woman and man doing a plank high five in the gym"></div>
    <div class="post-bar abs">
      <p class="post-text abs">Lorem Ipsum is simply dummy text of the printing and typesetting industry Lorem Ipsum.</p>
      <svg class="post-go abs" viewBox="0 0 46 46"><circle cx="23" cy="23" r="23" fill="#fff"/><path d="M14 23h17M24 15l8 8-8 8" fill="none" stroke="#222" stroke-width="3.5" stroke-linecap="round" stroke-linejoin="round"/></svg>
    </div>
  </article>
</section>

<section class="testimonials abs">
  <h2 class="testi-title heading abs">TESTIMONIALS</h2>
  <svg class="testi-quote abs" width="64" height="52" viewBox="0 0 64 52" fill="#e8322a"><path d="M4 52V28C4 12 12 4 26 2v10c-7 2-10 6-10 14h10v26zM36 52V28C36 12 44 4 58 2v10c-7 2-10 6-10 14h10v26z"/></svg>
  <p class="testi-copy abs">Lorem Ipsum is simply dummy text of the printing and typesetting industry. Lorem Ipsum has been the industry's standard dummy text ever since the 1500s, when an unknown printer took a galley of type and scrambled.</p>
  <p class="testi-name abs">- CLIENT NAME</p>
  <div class="testi-dots abs"><span class="on"></span><span></span><span></span></div>
  <div class="testi-photo abs" role="img" aria-label="Woman lifting a barbell, red tinted"></div>
</section>

<section>
  <h2 class="contact-title heading abs">CONTACT <span class="deep">US</span></h2>
  <div class="field abs" style="left:232px;top:3232px;width:353px">Name</div>
  <div class="field abs" style="left:615px;top:3232px;width:356px">Email</div>
  <div class="field abs" style="left:232px;top:3292px;width:353px">Phone</div>
  <div class="field abs" style="left:615px;top:3292px;width:356px">Address</div>
  <div class="field abs" style="left:232px;top:3384px;width:739px">Message</div>
  <div class="send abs">SEND NOW</div>
</section>

<footer class="footer abs">
  <span class="social abs" style="left:544px"></span>
  <span class="social abs" style="left:604px"></span>
  <p class="copyright abs">©BOLD ORCHID. 2018 · All Rights Reserved.</p>
</footer>

</body>
</html>
```